label design for soy candle

I am a start up making soy candles and other products involving scents.
On the label should be in writing : the scent, Handgemacht in der Schweiz, Sojakerze, my logo with the name Thorvel Candles on it. I will upload the currant label of my candles, but I want something more fashioned. The color of the label should be black with the scent written in gold, and the rest in white. Or maybe suggest something different, I am open to new designs. I am also open to change the logo, except the flower has to stay.
Sizes : square 60x60mm / round 50mm / rectangle 70x20mm ( for different jars )

```html
<!DOCTYPE html>
<html lang="de">
<head>
<meta charset="utf-8">
<title>Pink Hibiscus – Sojakerze Etikett</title>
<link rel="stylesheet" href="https://fonts.googleapis.com/css2?family=Sacramento&family=Tinos&family=Arimo:wght@400&display=swap">
<style>
  :root {
    --backdrop: #b3abc0;
    --label-black: #000000;
    --peach: #f0b39f;
    --blush: #f6d9d6;
    --lavender: #e2d3ec;
    --text-white: #ffffff;
  }
  html, body {
    margin: 0;
    padding: 0;
    width: 1200px;
    height: 1200px;
    overflow: hidden;
    background: var(--backdrop);
  }
  .canvas {
    position: relative;
    width: 1200px;
    height: 1200px;
  }
  .label {
    position: absolute;
    left: 100px;
    top: 100px;
    width: 1000px;
    height: 1000px;
  }
  .pattern-border {
    position: absolute;
    inset: 0;
    background: linear-gradient(90deg, var(--peach) 0%, #f3c6bb 45%, var(--blush) 70%, var(--lavender) 100%);
  }
  .panel {
    position: absolute;
    inset: 59px;
    background: var(--label-black);
  }
  .frame {
    position: absolute;
    inset: 105px;
    border: 16px solid;
    border-image: linear-gradient(135deg, var(--peach) 0%, #fbe6e2 45%, var(--blush) 65%, var(--lavender) 100%) 1;
  }
  .brand {
    position: absolute;
    left: 0;
    right: 0;
    top: 196px;
    display: flex;
    flex-direction: column;
    align-items: center;
    gap: 28px;
  }
  .brand-mark {
    width: 64px;
    height: 64px;
    border-radius: 50%;
    background: var(--text-white);
  }
  .brand-name {
    font-family: "Arimo", sans-serif;
    font-size: 20px;
    line-height: 22px;
    letter-spacing: 0.3px;
    color: var(--text-white);
  }
  .scent-name {
    position: absolute;
    left: 0;
    right: 0;
    top: 372px;
    margin: 0;
    text-align: center;
    font-family: "Sacramento", cursive;
    font-weight: 400;
    font-size: 178px;
    line-height: 158px;
    background: linear-gradient(90deg, var(--peach) 25%, #f7d2cb 55%, var(--lavender) 80%);
    -webkit-background-clip: text;
    background-clip: text;
    color: transparent;
  }
  .scent-name span {
    display: block;
  }
  .scent-name .line-one {
    padding-right: 40px;
  }
  .product-info {
    position: absolute;
    left: 0;
    right: 0;
    top: 752px;
    text-align: center;
    font-family: "Tinos", serif;
    font-size: 26px;
    line-height: 30px;
    color: var(--text-white);
  }
</style>
</head>
<body>
  <div class="canvas">
    <div class="label">
      <div class="pattern-border" role="img" aria-label="Geometrisches Sternlinienmuster in Roségold auf Pfirsich-Lavendel-Verlauf"></div>
      <div class="panel"></div>
      <div class="frame"></div>
      <div class="brand">
        <div class="brand-mark"></div>
        <div class="brand-name">THORVEL CANDLES</div>
      </div>
      <h1 class="scent-name"><span class="line-one">Pink</span><span>Hibiscus</span></h1>
      <div class="product-info">SOJAKERZE<br>HANDGEMACHT</div>
    </div>
  </div>
</body>
</html>
```